Modern, Clean, Edgy & Fun Comedy Show Flyer

We need to a create a new flyer for the comedy show, Harbor Laugh Night. The original version of the flyer is attached (file: Old flyer), as well as two versions of the logo.
- The text should be the same except now the show is Every First Wednesday and the next show is June 1.
- Remove the jerk shop logo
- Remove the picture of the man, and replace it with a photo of Delphine (our host), the Audience, or something of your own design.
* pictures of Delphine and the Audience is attached.
* We'd like to keep the same color palette and have also attached a color palette for reference

I have also attached 4 references of flyers that I like, that you can use to get an idea of the theme and aesthetic we are looking for.
* Files: Reference 1, Reference 2, Reference 3, Reference 4
Updates

Colors
3277b5
85acd3
0455a3
eaf1f7
cee9f5
ecf7fb
d5d5d5
e6e6e6

Requirements
Must have
• The harbor laugh night logo attached
• The text as specified in the project description
• An option with Delphine and without

```html
<!DOCTYPE html>
<html lang="en">
<head>
<meta charset="utf-8">
<title>Harbor Laugh Night – Comedy Show Every 1st Wednesday</title>
<link rel="stylesheet" href="https://fonts.googleapis.com/css2?family=Oswald:wght@700&family=Didact+Gothic&family=Arimo:wght@400;700&display=swap">
<style>
  :root {
    --paper: #e9eded;
    --line-white: #ffffff;
    --line-ice: #cee9f5;
    --ink: #111111;
    --ink-soft: #333333;
    --brand-blue: #2d55d8;
    --star-blue: #3277b5;
    --address-blue: #3a5ea8;
    --photo-deep: #2a1a12;
    --photo-warm: #7a4a30;
  }
  * { margin: 0; padding: 0; box-sizing: border-box; }
  html, body { width: 1200px; height: 800px; overflow: hidden; background: var(--paper); }
  .flyer {
    position: relative;
    width: 1200px;
    height: 800px;
    background: var(--paper);
    overflow: hidden;
    font-family: "Didact Gothic", sans-serif;
  }
  .backdrop { position: absolute; inset: 0; }
  .headline {
    position: absolute;
    left: 30px;
    top: 4px;
    font-family: "Oswald", sans-serif;
    font-weight: 700;
    color: var(--ink);
    text-transform: uppercase;
    line-height: 1;
  }
  .headline__line1 { display: block; font-size: 66px; letter-spacing: 1px; }
  .headline__line2 { display: block; font-size: 78px; letter-spacing: 1px; margin-top: -2px; }
  .host-photo {
    position: absolute;
    left: 40px;
    top: 150px;
    width: 660px;
    height: 650px;
    background:
      radial-gradient(ellipse 48% 52% at 50% 50%, var(--photo-warm) 0%, var(--photo-deep) 60%, rgba(42,26,18,0.85) 80%, rgba(233,237,237,0) 100%);
  }
  .brand-name {
    position: absolute;
    left: 770px;
    top: 52px;
    width: 360px;
    text-align: center;
    font-family: "Didact Gothic", sans-serif;
    font-size: 46px;
    line-height: 1.1;
    color: var(--brand-blue);
  }
  .lineup {
    position: absolute;
    left: 770px;
    top: 276px;
  }
  .lineup__title {
    font-size: 37px;
    color: var(--ink-soft);
    letter-spacing: 1px;
    margin-left: 12px;
    margin-bottom: 10px;
  }
  .lineup__list { list-style: none; }
  .lineup__item {
    display: flex;
    align-items: center;
    height: 40.5px;
    font-size: 25px;
    color: var(--ink-soft);
    letter-spacing: 0.5px;
  }
  .lineup__item--accent { color: var(--brand-blue); }
  .lineup__star { width: 20px; height: 20px; margin-right: 18px; flex: none; }
  .details {
    position: absolute;
    left: 730px;
    top: 532px;
    width: 440px;
    text-align: center;
  }
  .details__host {
    font-size: 30px;
    color: var(--ink);
    letter-spacing: 0.5px;
    margin-bottom: 18px;
  }
  .details__date {
    font-family: "Arimo", sans-serif;
    font-weight: 700;
    font-size: 34px;
    color: var(--brand-blue);
    margin-bottom: 6px;
  }
  .details__venue, .details__address, .details__entry {
    font-family: "Arimo", sans-serif;
    font-size: 24px;
    line-height: 40px;
  }
  .details__venue { color: var(--ink-soft); }
  .details__address { color: var(--address-blue); font-weight: 700; }
  .details__entry { color: var(--ink-soft); font-weight: 700; }
</style>
</head>
<body>
<main class="flyer">
  <svg class="backdrop" width="1200" height="800" viewBox="0 0 1200 800" aria-hidden="true">
    <g fill="none" stroke-linejoin="miter">
      <polyline points="700,0 560,170 760,250 1200,120" stroke="var(--line-white)" stroke-width="12"/>
      <polyline points="0,60 240,0" stroke="var(--line-white)" stroke-width="10"/>
      <polyline points="0,260 170,120 420,330 0,470" stroke="var(--line-white)" stroke-width="12"/>
      <polyline points="760,250 700,430 900,330 700,560 1000,500" stroke="var(--line-white)" stroke-width="10"/>
      <polyline points="0,560 250,800" stroke="var(--line-white)" stroke-width="10"/>
      <polygon points="720,230 780,0 800,0 750,240" fill="var(--line-ice)" stroke="none"/>
      <polyline points="1170,250 1020,800" stroke="var(--line-ice)" stroke-width="18"/>
      <polyline points="1040,120 1200,90" stroke="var(--line-ice)" stroke-width="14"/>
      <polyline points="880,250 1170,250" stroke="var(--line-ice)" stroke-width="14"/>
    </g>
  </svg>

  <h1 class="headline">
    <span class="headline__line1">Comedy Show Every</span>
    <span class="headline__line2">1st Wednesday</span>
  </h1>

  <div class="host-photo" role="img" aria-label="Photo of the host smiling and holding a microphone on stage"></div>

  <p class="brand-name">Harbor Laugh Night</p>

  <section class="lineup">
    <h2 class="lineup__title">Featuring . . .</h2>
    <ul class="lineup__list">
      <li class="lineup__item"><svg class="lineup__star" viewBox="0 0 20 20" aria-hidden="true"><polygon points="10,1 12.6,7.2 19.3,7.5 14.1,11.7 15.9,18.3 10,14.5 4.1,18.3 5.9,11.7 0.7,7.5 7.4,7.2" fill="var(--star-blue)"/></svg>Warren Tillbrook</li>
      <li class="lineup__item lineup__item--accent"><svg class="lineup__star" viewBox="0 0 20 20" aria-hidden="true"><polygon points="10,1 12.6,7.2 19.3,7.5 14.1,11.7 15.9,18.3 10,14.5 4.1,18.3 5.9,11.7 0.7,7.5 7.4,7.2" fill="var(--star-blue)"/></svg>Reed Calloway</li>
      <li class="lineup__item"><svg class="lineup__star" viewBox="0 0 20 20" aria-hidden="true"><polygon points="10,1 12.6,7.2 19.3,7.5 14.1,11.7 15.9,18.3 10,14.5 4.1,18.3 5.9,11.7 0.7,7.5 7.4,7.2" fill="var(--star-blue)"/></svg>Milo Brackenridge</li>
      <li class="lineup__item lineup__item--accent"><svg class="lineup__star" viewBox="0 0 20 20" aria-hidden="true"><polygon points="10,1 12.6,7.2 19.3,7.5 14.1,11.7 15.9,18.3 10,14.5 4.1,18.3 5.9,11.7 0.7,7.5 7.4,7.2" fill="var(--star-blue)"/></svg>Ravi Kumaran</li>
      <li class="lineup__item"><svg class="lineup__star" viewBox="0 0 20 20" aria-hidden="true"><polygon points="10,1 12.6,7.2 19.3,7.5 14.1,11.7 15.9,18.3 10,14.5 4.1,18.3 5.9,11.7 0.7,7.5 7.4,7.2" fill="var(--star-blue)"/></svg>Tessa Okonjo</li>
    </ul>
  </section>

  <section class="details">
    <p class="details__host">Hosted by Delphine Arvell</p>
    <p class="details__date">MONDAY, APRIL 4</p>
    <p class="details__venue">The Tin Crate</p>
    <p class="details__address">29 Pierhouse Lane, Harborview</p>
    <p class="details__entry">Adm:&nbsp; FREE | DOORS 6:30 PM</p>
  </section>
</main>
</body>
</html>
```